Business card design needed

We are a Custom Joinery and specialise in design, Manufacture and Installation of kitchens and cabinetry
We currently have a logo based on the northern star in red and black but are open to something that would look fresh and clean
Updates

Project Deadline Extended
Reason: Need a couple days to go through designs. Finding some designs that are great on front and others great on reverse. I would like to be able to comment and get the total look we are after.

Target Market(s)

30-50 year olds who are looking to renovate

Industry/Entity Type

Business

Contact Information for Business Card

Maple Crest Interiors
ABN 37 418 260 503
Carlo Whitby - Cabinetmaker/Designer Licence No. 581907K

Requirements
Nice to have
• Maybe a nice fresh modern kitchen picture

```html
<!DOCTYPE html>
<html lang="en">
<head>
<meta charset="utf-8">
<title>Maple Crest Interiors – Business Cards</title>
<link rel="stylesheet" href="https://fonts.googleapis.com/css2?family=Jost:wght@400;500;600;700&display=swap">
<style>
  :root {
    --red: #c8202c;
    --ink: #2e2e30;
    --paper: #ffffff;
    --stage: #e8e5e1;
    --photo-light: #d9d9d9;
    --photo-dark: #8a8a8a;
  }
  * { margin: 0; padding: 0; box-sizing: border-box; }
  html, body { width: 1200px; height: 729px; overflow: hidden; }
  body {
    background: var(--stage);
    font-family: "Jost", sans-serif;
    position: relative;
  }
  .card {
    position: absolute;
    width: 528px;
    height: 300px;
    overflow: hidden;
    box-shadow: 0 2px 6px rgba(0,0,0,0.18);
  }
  .card--front { left: 51px; top: 25px; background: var(--paper); }
  .card--back-white { left: 609px; top: 25px; background: var(--paper); }
  .card--back-photo { left: 53px; top: 375px; }
  .card--back-red { left: 623px; top: 378px; background: var(--red); }

  /* front */
  .brand {
    position: absolute; left: 36px; top: 48px;
    display: flex; align-items: center; gap: 12px;
    font-size: 26px; font-weight: 500; letter-spacing: 1px;
    color: var(--ink); text-transform: uppercase; line-height: 1;
  }
  .brand__square { width: 18px; height: 18px; background: var(--red); }
  .holder {
    position: absolute; left: 31px; top: 181px;
    font-size: 15px; color: var(--ink);
  }
  .holder__name { font-size: 19px; font-weight: 600; color: var(--red); letter-spacing: 0.4px; }
  .phone {
    position: absolute; left: 31px; top: 222px;
    display: flex; align-items: center; gap: 6px;
    font-size: 16px; color: var(--ink);
  }
  .swoosh { position: absolute; left: 0; top: 0; width: 528px; height: 300px; }
  .address {
    position: absolute; right: 30px; top: 236px;
    text-align: right; color: var(--paper);
    font-size: 15px; line-height: 20px;
  }
  .registration {
    position: absolute; right: 30px; top: 279px;
    color: var(--paper); font-size: 11px;
  }

  /* backs */
  .back-name {
    position: absolute; left: 0; right: 0; top: 112px;
    text-align: center; font-size: 30px; font-weight: 500;
    letter-spacing: 1.5px; text-transform: uppercase;
  }
  .back-url {
    position: absolute; left: 0; right: 0; bottom: 14px;
    text-align: center; font-size: 20px; font-weight: 600; letter-spacing: 1.2px;
  }
  .card--back-white .back-name, .card--back-white .back-url { color: var(--ink); }
  .card--back-photo .back-name, .card--back-photo .back-url,
  .card--back-red .back-name, .card--back-red .back-url { color: var(--paper); }
  .kitchen-photo {
    position: absolute; inset: 0;
    background:
      linear-gradient(180deg, rgba(200,32,44,0) 0%, rgba(200,32,44,0) 55%, rgba(170,40,44,0.55) 62%, rgba(150,40,40,0.6) 88%, rgba(80,80,80,0.6) 100%),
      linear-gradient(90deg, var(--photo-dark) 0%, var(--photo-light) 55%, #f2f2f2 100%);
  }
</style>
</head>
<body>

  <section class="card card--front">
    <div class="brand"><span class="brand__square"></span>Maple Crest Interiors</div>
    <p class="holder"><span class="holder__name">Carlo Whitby,</span> Cabinetmaker/Designer</p>
    <p class="phone">
      <svg width="12" height="14" viewBox="0 0 12 14" aria-hidden="true">
        <path d="M2 0.5 L4.5 0.5 L5.2 4 L3.6 5.2 C4.3 7.3 5.4 8.8 7 9.8 L8.4 8.5 L11.5 9.6 L11 13 C5 13.5 0.5 7.5 1 1.5 Z" fill="var(--red)"/>
      </svg>
      0140-552-873
    </p>
    <svg class="swoosh" viewBox="0 0 528 300" aria-hidden="true">
      <path d="M0 282 C150 262 320 215 528 220 L528 300 L0 300 Z" fill="var(--red)"/>
      <path d="M0 258 C150 262 300 232 528 228 L528 236 C320 240 160 278 0 290 Z" fill="var(--ink)"/>
      <path d="M170 262 C280 238 390 218 500 212 C390 224 290 246 200 266 Z" fill="var(--red)"/>
      <path d="M210 262 C310 240 400 226 470 220 C400 232 310 250 230 266 Z" fill="var(--red)"/>
    </svg>
    <p class="address">12, Harbour Court<br>Riverton, State 0042</p>
    <p class="registration">ABN 37 418 260 503 &amp; Licence No. 581907K</p>
  </section>

  <section class="card card--back-white">
    <p class="back-name">Maple Crest Interiors</p>
    <p class="back-url">www.maplecrestinteriors.com</p>
  </section>

  <section class="card card--back-photo">
    <div class="kitchen-photo" role="img" aria-label="Photo of a modern kitchen with red gloss cabinets and a steel bar table"></div>
    <p class="back-name">Maple Crest Interiors</p>
    <p class="back-url">www.maplecrestinteriors.com</p>
  </section>

  <section class="card card--back-red">
    <p class="back-name">Maple Crest Interiors</p>
    <p class="back-url">www.maplecrestinteriors.com</p>
  </section>

</body>
</html>
```